Animal Horse & Bedding Company Needs a Website Coded & Designed

We need a website for a new animal bedding and feed company that is visually grabbing and vibrant. We would like to see a website that displays trust, quality and confidence. Needs to be responsive and mobile friendly for all browsers and coded for both Android & IOS. SEO is also important.

Joomla or Wordpress – must be both desktop and mobile friendly with fast page load speed. Need the ability to edit ourselves in Wordpress or Joomla.

Full details attached below with some layout and content ideas.

Coding

Coded - Design and coding required

Number of Pages Required

5+ page

Font styles to use
Sans Serif

Requirements
Must have
• Needs to be responsive and mobile friendly for all browsers and coded for both Android & IOS. SEO is also important.

Wordpress – must be both desktop and mobile friendly with fast page load speed. Need the ability to edit ourselves in Wordpress.

Logo Colours:
Dark Brown
CMYK: 50 / 70 / 80 / 70
Pantone: 4625C

Orange
CMYK: 0 / 50 / 100 / 0
Pantone: 144C
Nice to have
• Use picture of building attached and super impose logo on building.

```html
<!DOCTYPE html>
<html lang="en">
<head>
<meta charset="utf-8">
<title>Haybarn &amp; Co. — Animal Bedding</title>
<link href="https://fonts.googleapis.com/css2?family=Montserrat:wght@300;400;500;600;700&display=swap" rel="stylesheet">
<style>
:root{
  --brown:#3b1a10;
  --brown-deep:#2c120a;
  --orange:#f0841f;
  --orange-dark:#d96f14;
  --white:#ffffff;
  --ink:#222222;
  --grey:#8a8a8a;
  --light:#f4f4f4;
}
*{box-sizing:border-box;margin:0;padding:0}
html,body{width:1200px;height:3158px;overflow:hidden}
body{font-family:'Montserrat',sans-serif;color:var(--ink);background:var(--white);position:relative}
section,header,footer{position:relative;width:1200px;overflow:hidden}
.btn{display:inline-block;background:var(--orange);color:var(--white);font-size:10px;font-weight:500;text-transform:uppercase;letter-spacing:.5px;text-align:center}

/* header */
.site-header{height:51px;background:var(--white)}
.brand{position:absolute;left:0;top:0;width:245px;height:51px;background:var(--brown);display:flex;align-items:center;gap:10px;padding-left:28px}
.brand-dot{width:16px;height:16px;border-radius:50%;background:var(--orange)}
.brand-name{color:var(--white);font-size:15px;font-weight:600;letter-spacing:1px;text-transform:uppercase}
.social{position:absolute;left:856px;top:19px;display:flex;gap:21px}
.social span{width:12px;height:12px;border-radius:50%;border:1.5px solid var(--brown)}
.call-box{position:absolute;right:0;top:0;width:207px;height:51px;background:var(--orange);color:var(--white);text-align:center;font-size:11px;font-weight:700;letter-spacing:.6px;padding-top:11px;line-height:16px}

/* hero */
.hero{height:411px}
.hero-photo{position:absolute;inset:0;background:radial-gradient(ellipse at 55% 45%,#5a2f18 0%,#7a4618 40%,#b8741f 75%,#8d5a1a 100%)}
.hero-shade{position:absolute;inset:0;background:rgba(40,18,8,.25)}
.hero-content{position:absolute;left:0;right:0;top:120px;text-align:center;color:var(--white)}
.hero-title{font-size:68px;font-weight:700;line-height:80px}
.hero-title em{font-style:normal;color:var(--orange)}
.hero-tagline{font-size:27px;font-weight:500;margin-top:14px}
.hero-content .btn{margin-top:22px;width:190px;height:34px;line-height:34px;font-size:11px}
.slider-dots{position:absolute;left:1090px;top:160px;display:flex;flex-direction:column;gap:11px}
.slider-dots span{width:8px;height:8px;border-radius:50%;background:var(--orange)}
.slider-dots span:first-child{background:transparent;border:1.5px solid var(--orange)}

/* intro */
.intro{height:318px}
.intro-gallery{position:absolute;left:79px;top:30px;display:grid;grid-template-columns:198px 198px;grid-template-rows:114px 114px;gap:12px 14px}
.intro-gallery div{width:198px;height:114px}
.g-rabbit{background:linear-gradient(135deg,#6f8a3a,#a4894f)}
.g-piglets{background:linear-gradient(135deg,#c9a087,#e4c1a9)}
.g-cat{background:linear-gradient(135deg,#4b4b4b,#9a9a9a)}
.g-lamb{background:linear-gradient(135deg,#7d9a3e,#ecebe2)}
.intro-text{position:absolute;left:535px;top:30px;width:560px}
.intro-text h2{font-size:27px;font-weight:700;line-height:30px;color:var(--ink)}
.rule{width:95px;height:2px;background:var(--orange);margin:12px 0 18px}
.intro-text p{font-size:9.5px;line-height:15px;color:var(--grey);width:540px}
.intro-text p + p{margin-top:8px}
.intro-text .btn{margin-top:16px;width:140px;height:24px;line-height:24px;font-size:9px}

/* benefits */
.benefits{height:366px;color:var(--white)}
.benefits-photo{position:absolute;inset:0;background:linear-gradient(90deg,#5a2c17 0%,#7a3d1e 45%,#a65a2a 75%,#6b3a20 100%)}
.benefits-inner{position:absolute}
.benefits h3{font-size:26px;font-weight:700;letter-spacing:.3px}
.benefits .rule{width:120px;background:var(--white);height:1.5px;margin:14px 0 20px}
.benefit-list{list-style:none}
.benefit-list li{font-size:14.5px;font-weight:300;line-height:26.5px;padding-left:25px;position:relative}
.benefit-list li::before{content:"";position:absolute;left:0;top:11px;width:5px;height:5px;border-radius:50%;background:var(--orange)}
.benefit-list li.plain::before{display:none}
.benefits .btn{margin:6px 0 0 25px;width:140px;height:22px;line-height:22px;font-size:9px}
.benefits-straw .benefits-inner{left:117px;top:48px}
.benefits-feed{height:372px}
.benefits-feed .benefits-photo{background:linear-gradient(90deg,#3b2a10 0%,#6b4a1a 30%,#4a2f10 55%,#2b1a08 100%)}
.benefits-feed .benefits-inner{left:624px;top:46px}
.benefits-feed .rule{margin:14px 0 18px}
.benefits-feed .benefit-list li{font-size:14px;line-height:21.5px}
.benefits-feed .benefit-list li::before{top:8px}

/* products */
.products{height:749px;background:var(--white)}
.section-title{position:absolute;left:0;right:0;text-align:center;font-size:27px;font-weight:600}
.section-title::after{content:"";display:block;width:110px;height:2px;background:var(--orange);margin:12px auto 0}
.products .section-title{top:58px;font-weight:500}
.card{position:absolute;width:263px;height:235px;background:var(--white);box-shadow:0 2px 12px rgba(0,0,0,.14);overflow:visible}
.price{position:absolute;left:-10px;top:10px;width:158px;height:33px;line-height:33px;background:var(--orange-dark);color:var(--white);font-size:17px;font-style:italic;font-weight:300;padding-left:28px;border-radius:0 18px 18px 18px}
.pack{position:absolute;left:67px;top:48px;width:125px;height:102px}
.pack-purple{background:linear-gradient(180deg,#3fa7d8 0%,#b12b9a 45%,#c23aa6 100%);border-radius:6px}
.pack-red{background:linear-gradient(180deg,#f5f1ea 0%,#e5482a 50%,#f07a26 100%);border-radius:4px}
.pack-grey{background:linear-gradient(180deg,#f1f1f1 0%,#c9ccd2 50%,#2c3d6b 100%);border-radius:4px}
.card-name{position:absolute;left:24px;top:166px;font-size:11px;font-weight:500}
.stars{position:absolute;right:30px;top:162px;color:var(--orange);font-size:12px;letter-spacing:1px}
.fav{position:absolute;left:24px;top:190px;width:22px;height:22px;border:1.5px solid var(--orange)}
.fav svg{display:block;margin:4px auto 0}
.card .btn{position:absolute;left:60px;top:192px;width:110px;height:18px;line-height:18px;font-size:7px}
.card-corner{position:absolute;right:0;bottom:0;width:0;height:0;border-left:38px solid transparent;border-bottom:38px solid var(--orange-dark)}
.view-all{position:absolute;left:526px;top:707px;width:140px;height:26px;line-height:26px}

/* testimonials */
.testimonials{height:556px}
.testimonials .section-title{top:68px}
.quote{position:absolute;top:158px;width:303px;height:276px;background:var(--white);box-shadow:0 2px 12px rgba(0,0,0,.14);text-align:center;padding:26px 42px 0}
.quote .q-stars{color:var(--orange);font-size:19px;letter-spacing:4px}
.quote p{font-size:10.5px;line-height:15.5px;color:#555;margin-top:10px}
.avatar{width:58px;height:58px;border-radius:50%;margin:14px auto 0;background:radial-gradient(circle at 50% 40%,#d9c3b3,#6d5a52)}
.q-name{font-size:10.5px;font-weight:600;margin-top:10px}
.q-place{font-size:9px;color:var(--orange);margin-top:8px}
.testimonials .btn{position:absolute;left:530px;top:492px;width:142px;height:26px;line-height:26px}

/* newsletter */
.newsletter{height:78px;background:linear-gradient(180deg,var(--white) 0%,var(--white) 62%,var(--brown) 62%)}
.newsletter-bar{position:absolute;left:89px;top:0;width:1088px;height:78px;background:var(--orange-dark);display:flex;align-items:center}
.newsletter-label{color:var(--white);font-size:13px;width:290px;padding-left:44px}
.newsletter-input{width:540px;height:40px;background:var(--white);font-size:12px;color:#666;line-height:40px;padding-left:12px}
.newsletter-submit{width:156px;height:40px;background:var(--brown-deep);color:var(--white);font-size:13px;text-align:center;line-height:40px}

/* footer */
.site-footer{height:257px;background:var(--brown);color:var(--white)}
.f-about{position:absolute;left:70px;top:44px;width:240px}
.f-brand{display:flex;align-items:center;gap:8px;margin-bottom:16px;padding-left:14px}
.f-brand .brand-dot{width:14px;height:14px}
.f-brand span{font-size:14px;font-weight:600;letter-spacing:1px;text-transform:uppercase}
.f-about p{font-size:10px;line-height:16px;font-weight:300}
.f-social{display:flex;gap:36px;margin-top:14px;padding-left:6px}
.f-social span{width:12px;height:12px;border-radius:50%;border:1.5px solid var(--white)}
.f-col{position:absolute;top:50px}
.f-col h4{font-size:17px;font-weight:400;margin-bottom:12px}
.f-col ul{list-style:none}
.f-col li{font-size:10px;line-height:17px;padding-left:33px;position:relative}
.f-col li::before{content:"";position:absolute;left:2px;top:6px;width:5px;height:5px;border-radius:50%;background:var(--orange)}
.f-products{left:362px}
.f-care{left:600px;top:47px}
.f-care li{line-height:21px}
.f-care li::before{top:8px}
.f-contact{left:858px;top:46px}
.f-contact h4{margin-bottom:2px}
.f-phone{color:var(--orange);font-size:17px}
.f-link{display:flex;align-items:center;gap:18px;font-size:16px;margin-top:24px;padding-left:6px}
.f-link + .f-link{margin-top:20px}
.f-bottom{position:absolute;left:70px;right:56px;top:222px;border-top:1px solid rgba(255,255,255,.2);text-align:center;font-size:10px;padding-top:12px;font-weight:300}
</style>
</head>
<body>

<header class="site-header">
  <div class="brand"><span class="brand-dot"></span><span class="brand-name">Haybarn &amp; Co.</span></div>
  <div class="social" aria-label="Social links"><span></span><span></span><span></span><span></span></div>
  <div class="call-box">CALL US TODAY !<br>555-0142-778</div>
</header>

<section class="hero">
  <div class="hero-photo" role="img" aria-label="Girl with a dark horse among golden autumn trees"></div>
  <div class="hero-shade"></div>
  <div class="hero-content">
    <h1 class="hero-title">Welcome to <em>animals</em><br><em>bedding</em> Company</h1>
    <p class="hero-tagline">HAPPY PETS MAKE LIFE BETTER!</p>
    <span class="btn">Contact Us</span>
  </div>
  <div class="slider-dots"><span></span><span></span><span></span><span></span></div>
</section>

<section class="intro">
  <div class="intro-gallery">
    <div class="g-rabbit" role="img" aria-label="Rabbit sitting on grass"></div>
    <div class="g-piglets" role="img" aria-label="Piglets resting on straw"></div>
    <div class="g-cat" role="img" aria-label="Cat eating from a bowl"></div>
    <div class="g-lamb" role="img" aria-label="White lamb lying on grass"></div>
  </div>
  <div class="intro-text">
    <h2>The bedding that’s kind to<br>your animals</h2>
    <div class="rule"></div>
    <p>Your animal deserves the very best in health and comfort to keep them healthy, strong and happy. Our products are designed for horses, livestock (goats, cattle and sheep), small caged animals (rabbits, guinea pigs and more) Your animal deserves the very best in health and comfort to keep them healthy, strong and happy. Our products are designed for horses, livestock (goats, cattle and sheep), small caged animals (rabbits, guinea pigs and more).</p>
    <p>QUALITY GUARANTEED Grown for quality - 100% natural with no chemicals or additives<br>FULL SERVICE SOLUTION</p>
    <span class="btn">Learn More</span>
  </div>
</section>

<section class="benefits benefits-straw">
  <div class="benefits-photo" role="img" aria-label="White horse galloping in a field at sunset"></div>
  <div class="benefits-inner">
    <h3>BEDDING BENEFITS</h3>
    <div class="rule"></div>
    <ul class="benefit-list">
      <li>100% Natural Chopped Straw</li>
      <li>Low Dust</li>
      <li>Chemical &amp; Additive Free</li>
      <li>Clean &amp; Highly Absorbent</li>
      <li>Cheaper than Wood Shavings</li>
      <li class="plain">Economic – less used and less wasted</li>
      <li class="plain">Environmentally Friendly – Recyclable &amp; Compostable</li>
    </ul>
    <span class="btn">Learn More</span>
  </div>
</section>

<section class="products">
  <h2 class="section-title">Our Products</h2>

  <article class="card" style="left:126px;top:145px">
    <div class="price">$109.00</div>
    <div class="pack pack-purple" role="img" aria-label="Cat food can"></div>
    <div class="card-name">MEADOW BITES</div><div class="stars">★★★★★</div>
    <div class="fav"><svg width="11" height="10" viewBox="0 0 11 10"><path d="M5.5 9 1.2 4.8A2.4 2.4 0 0 1 5.5 1.6a2.4 2.4 0 0 1 4.3 3.2Z" fill="none" stroke="#f0841f" stroke-width="1"/></svg></div>
    <span class="btn">Add to card</span><div class="card-corner"></div>
  </article>
  <article class="card" style="left:473px;top:145px">
    <div class="price">$109.00</div>
    <div class="pack pack-red" role="img" aria-label="Horse feed bag"></div>
    <div class="card-name">TRAIL MUESLI</div><div class="stars">★★★★★</div>
    <div class="fav"><svg width="11" height="10" viewBox="0 0 11 10"><path d="M5.5 9 1.2 4.8A2.4 2.4 0 0 1 5.5 1.6a2.4 2.4 0 0 1 4.3 3.2Z" fill="none" stroke="#f0841f" stroke-width="1"/></svg></div>
    <span class="btn">Add to card</span><div class="card-corner"></div>
  </article>
  <article class="card" style="left:820px;top:145px">
    <div class="price">$109.00</div>
    <div class="pack pack-grey" role="img" aria-label="Feed bag with horse image"></div>
    <div class="card-name">MEADOW BITES</div><div class="stars">★★★★★</div>
    <div class="fav"><svg width="11" height="10" viewBox="0 0 11 10"><path d="M5.5 9 1.2 4.8A2.4 2.4 0 0 1 5.5 1.6a2.4 2.4 0 0 1 4.3 3.2Z" fill="none" stroke="#f0841f" stroke-width="1"/></svg></div>
    <span class="btn">Add to card</span><div class="card-corner"></div>
  </article>

  <article class="card" style="left:126px;top:413px">
    <div class="price">$109.00</div>
    <div class="pack pack-purple" role="img" aria-label="Cat food can"></div>
    <div class="card-name">MEADOW BITES</div><div class="stars">★★★★★</div>
    <div class="fav"><svg width="11" height="10" viewBox="0 0 11 10"><path d="M5.5 9 1.2 4.8A2.4 2.4 0 0 1 5.5 1.6a2.4 2.4 0 0 1 4.3 3.2Z" fill="none" stroke="#f0841f" stroke-width="1"/></svg></div>
    <span class="btn">Add to card</span><div class="card-corner"></div>
  </article>
  <article class="card" style="left:473px;top:413px">
    <div class="price">$109.00</div>
    <div class="pack pack-red" role="img" aria-label="Horse feed bag"></div>
    <div class="card-name">TRAIL MUESLI</div><div class="stars">★★★★★</div>
    <div class="fav"><svg width="11" height="10" viewBox="0 0 11 10"><path d="M5.5 9 1.2 4.8A2.4 2.4 0 0 1 5.5 1.6a2.4 2.4 0 0 1 4.3 3.2Z" fill="none" stroke="#f0841f" stroke-width="1"/></svg></div>
    <span class="btn">Add to card</span><div class="card-corner"></div>
  </article>
  <article class="card" style="left:820px;top:413px">
    <div class="price">$109.00</div>
    <div class="pack pack-grey" role="img" aria-label="Feed bag with horse image"></div>
    <div class="card-name">MEADOW BITES</div><div class="stars">★★★★★</div>
    <div class="fav"><svg width="11" height="10" viewBox="0 0 11 10"><path d="M5.5 9 1.2 4.8A2.4 2.4 0 0 1 5.5 1.6a2.4 2.4 0 0 1 4.3 3.2Z" fill="none" stroke="#f0841f" stroke-width="1"/></svg></div>
    <span class="btn">Add to card</span><div class="card-corner"></div>
  </article>

  <span class="btn view-all">View All</span>
</section>

<section class="benefits benefits-feed">
  <div class="benefits-photo" role="img" aria-label="Brown hare sitting in a sunlit meadow"></div>
  <div class="benefits-inner">
    <h3>BEDDING BENEFITS</h3>
    <div class="rule"></div>
    <ul class="benefit-list">
      <li>100% Natural</li>
      <li>Chemical &amp; Additive Free</li>
      <li>Available in Pellets or Cubes</li>
      <li>High Protein Content</li>
      <li>Eliminate Waste In Feeding</li>
      <li>Clean - Eliminates Dust From Feeding Baled Hay</li>
      <li>Cost Effective</li>
      <li class="plain">Convenient</li>
      <li class="plain">Less wasted feed</li>
    </ul>
    <span class="btn">Learn More</span>
  </div>
</section>

<section class="testimonials">
  <h2 class="section-title">TESTIMONIAL</h2>
  <article class="quote" style="left:56px">
    <div class="q-stars">★★★★★</div>
    <p>lorem ipsum dolor sit amet, consectetur adipiscing elit. nulla sed cum nunc, egestas placerat vulputate id vitae. a id pellentesque suspendisse tortor mi elementum interdum mauris venenatis.</p>
    <div class="avatar" role="img" aria-label="Customer portrait"></div>
    <div class="q-name">DANA WHITFIELD</div><div class="q-place">LAKEVIEW, ST</div>
  </article>
  <article class="quote" style="left:447px">
    <div class="q-stars">★★★★★</div>
    <p>lorem ipsum dolor sit amet, consectetur adipiscing elit. nulla sed cum nunc, egestas placerat vulputate id vitae. a id pellentesque suspendisse tortor mi elementum interdum mauris venenatis.</p>
    <div class="avatar" role="img" aria-label="Customer portrait"></div>
    <div class="q-name">DANA WHITFIELD</div><div class="q-place">LAKEVIEW, ST</div>
  </article>
  <article class="quote" style="left:839px">
    <div class="q-stars">★★★★★</div>
    <p>lorem ipsum dolor sit amet, consectetur adipiscing elit. nulla sed cum nunc, egestas placerat vulputate id vitae. a id pellentesque suspendisse tortor mi elementum interdum mauris venenatis.</p>
    <div class="avatar" role="img" aria-label="Customer portrait"></div>
    <div class="q-name">DANA WHITFIELD</div><div class="q-place">LAKEVIEW, ST</div>
  </article>
  <span class="btn">Learn More</span>
</section>

<section class="newsletter">
  <div class="newsletter-bar">
    <div class="newsletter-label">Subscribe Our Newsletter</div>
    <div class="newsletter-input">Enter your email</div>
    <div class="newsletter-submit">Subscribe</div>
  </div>
</section>

<footer class="site-footer">
  <div class="f-about">
    <div class="f-brand"><span class="brand-dot"></span><span>Haybarn &amp; Co.</span></div>
    <p>Haybarn &amp; Co. is a locally owned company located in Fernvale. We are dedicated in providing high quality products and services.</p>
    <div class="f-social"><span></span><span></span><span></span><span></span></div>
  </div>
  <div class="f-col f-products">
    <h4>PRODUCTS</h4>
    <ul><li>Cats</li><li>Dog</li><li>Rabit</li><li>Birds</li><li>sheep</li><li>pigs</li></ul>
  </div>
  <div class="f-col f-care">
    <h4>CUSTOMER CARE</h4>
    <ul><li>Home</li><li>Our Services</li><li>blog</li><li>About us</li><li>Contact Us</li></ul>
  </div>
  <div class="f-col f-contact">
    <h4>Call Now For Services!</h4>
    <div class="f-phone">555-010-2468</div>
    <div class="f-link"><svg width="16" height="12" viewBox="0 0 16 12"><rect x=".75" y=".75" width="14.5" height="10.5" fill="none" stroke="#fff" stroke-width="1.2"/><path d="M1 1l7 6 7-6" fill="none" stroke="#fff" stroke-width="1.2"/></svg>Email Us</div>
    <div class="f-link"><svg width="16" height="16" viewBox="0 0 16 16"><path d="M8 15s5-5.2 5-9A5 5 0 0 0 3 6c0 3.8 5 9 5 9Z" fill="none" stroke="#fff" stroke-width="1.2"/><circle cx="8" cy="6" r="1.8" fill="none" stroke="#fff" stroke-width="1.2"/></svg>Get Direction</div>
  </div>
  <div class="f-bottom">haybarn &amp; co. © 2021 All Rights Reserved. Terms of Use and Privacy Policy</div>
</footer>

</body>
</html>
```